Veridane Works, Inc. - Update our Website

Veridane Works needs a website to help our customers to navigate through our services efficiently. Our existing website is at www.verowk.example

We would like to explain our services with content and pictures (photographs) that distinguishes our products and services from our competition.

The website design must implement a strategy to focus on our Contract Labeling services.

With this new design we would like to attract new customers and ensure that our existing customers are fully informed with our latest offerings.

```html
<!DOCTYPE html>
<html lang="en">
<head>
<meta charset="utf-8">
<title>Veridane Works, Inc.</title>
<link href="https://fonts.googleapis.com/css2?family=Questrial&family=Montserrat:wght@800&display=swap" rel="stylesheet">
<style>
:root{
  --blue:#1479b8;
  --footer:#1673b2;
  --orange:#f08a00;
  --green:#6cbf16;
  --text:#555;
  --line:#dcdcdc;
  --panel:#f0f0f0;
  --dark:#222;
}
*{box-sizing:border-box;margin:0;padding:0}
html,body{width:1013px;height:1200px;overflow:hidden;background:#fff}
body{font-family:"Questrial",sans-serif;color:var(--text);position:relative}
.abs{position:absolute}
.site-header{left:0;top:0;width:1013px;height:79px}
.brand{left:62px;top:22px;display:flex;align-items:center;gap:10px}
.brand-mark{width:34px;height:34px;border-radius:50%;background:var(--green)}
.brand-name{font-family:"Montserrat",sans-serif;font-weight:800;font-size:17px;color:var(--dark);letter-spacing:.3px}
.main-nav{right:62px;top:40px;display:flex;gap:34px;font-size:10.6px;color:#444;text-transform:uppercase}
.main-nav .active{color:var(--blue)}
.hero{left:0;top:79px;width:1013px;height:372px;background:#000;overflow:hidden}
.hero-photo{position:absolute;left:400px;top:0;width:613px;height:372px;background:linear-gradient(90deg,#000 0%,#06252c 25%,#0e5a66 60%,#1a8a95 85%,#0f6470 100%)}
.hero-title{left:62px;top:85px;font-size:30px;color:var(--orange);letter-spacing:.2px}
.hero-text{left:62px;top:121px;width:420px;font-size:15.2px;line-height:22.6px;color:#fff}
.btn{display:inline-block;background:var(--green);color:#fff;text-transform:uppercase;font-size:10.5px;line-height:30px;padding:0 16px}
.hero-btn{left:62px;top:231px;height:36px;line-height:36px;color:#1a2a0a;font-size:11px;padding:0 13px}
.dots{left:62px;top:335px;display:flex;gap:7px}
.dots span{width:10px;height:10px;border-radius:2px;background:#fff}
.dots span:first-child{background:var(--blue)}
h2{font-weight:400;font-size:19px;color:var(--blue)}
h3{font-weight:400;font-size:14.5px;color:var(--orange)}
p{font-size:10.4px;line-height:15.6px}
.more{color:var(--green)}
.rule{height:1px;background:var(--line)}
.vrule{left:583px;top:486px;width:1px;height:600px;background:var(--line)}
.photo{border:1px solid #d0d0d0}
.service{display:flex;gap:24px}
.service .photo{width:114px;height:90px;flex:none}
.service h3{margin:0 0 5px}
.support{left:608px;top:881px;width:342px;height:205px;background:var(--panel);padding:18px}
.field{position:absolute;background:#fff;border:1px solid #c8c8c8;font-size:10.4px;color:#777;padding:6px 9px}
.site-footer{left:0;top:1102px;width:1013px;height:98px;background:var(--footer);color:#fff}
.foot-nav{left:62px;top:21px;display:flex;gap:32px;font-size:10.4px;text-transform:uppercase}
.copy{left:62px;top:60px;font-size:9.6px}
.social{left:830px;top:36px;display:flex;gap:7px}
.social span{width:25px;height:25px;border-radius:50%}
</style>
</head>
<body>
<header class="site-header abs">
  <div class="brand abs"><span class="brand-mark"></span><span class="brand-name">VERIDANE WORKS INC.</span></div>
  <nav class="main-nav abs"><span class="active">Home</span><span>About Us</span><span>Products</span><span>Services</span><span>User Support</span><span>Contact Us</span></nav>
</header>

<section class="hero abs">
  <div class="hero-photo" role="img" aria-label="Doctor in a lab coat reaching toward glowing medical cross icons on a teal background"></div>
  <h1 class="hero-title abs" style="font-weight:400">VERIDANE WORKS, INC.</h1>
  <p class="hero-text abs">Veridane Works, Inc. specializes in providing products and services to the pharmaceutical industry. We are focused on the needs of those individuals involved with Clinical Trial Materials.</p>
  <a class="btn hero-btn abs">View Product &amp; Services ››</a>
  <div class="dots abs"><span></span><span></span><span></span><span></span></div>
</section>

<section class="abs" style="left:62px;top:482px;width:509px">
  <h2>Welcome to Our Website</h2>
  <p style="margin-top:10px;line-height:18px">Vestibulum vel metus sit amet turpis bibendum tincidunt vel sit amet quam. Pellentesque habitant morbi tristique senectus et netus et malesuada fames ac turpis egestas. Nunc consequat congue nulla eu imperdiet. Donec in est erat, id malesuada turpis. Nunc a dui id turpis convallis semper. Nunc dignissim lectus vitae eros placerat euismod. Aenean lacinia sodales eros, sit amet molestie enim consectetur eget. Sed vel magna vel eros adipiscing adipiscing eu sit amet turpis. Mauris et massa sed lacus tempus pellentesque.</p>
  <a class="btn abs" style="left:0;top:152px;width:104px;text-align:center;padding:0">Read More ››</a>
</section>
<div class="rule abs" style="left:62px;top:682px;width:509px"></div>

<section class="abs" style="left:62px;top:697px;width:509px">
  <h2>Software Products / Services</h2>
  <div class="abs" style="left:1px;top:44px;width:227px">
    <div class="photo" style="height:90px;background:linear-gradient(90deg,#c8503a,#e8a070,#d94a5a,#f0c0a0)" role="img" aria-label="Prescription pills in bottles with an Rx label"></div>
    <h3 style="margin-top:10px">VeriPro/LBL™</h3>
    <p style="margin-top:4px">VeriPro/LBL™ is the industry's leading clinical label generation system offering superior overall capability and flexibility The system enables users to... <span class="more">Read More ››</span></p>
  </div>
  <div class="abs" style="left:281px;top:44px;width:228px">
    <div class="photo" style="height:90px;background:linear-gradient(135deg,#f4f6f8,#b8c8d8,#e8eef4,#9eb0c4)" role="img" aria-label="Stethoscope resting on a software disc"></div>
    <h3 style="margin-top:10px">Software Validation Services</h3>
    <p style="margin-top:4px">Veridane Works offers software validation services for the FDA regulated industry. Our knowledge of industry practices and standards...<span class="more">Read More ››</span></p>
  </div>
</section>
<div class="rule abs" style="left:62px;top:945px;width:509px"></div>

<section class="abs" style="left:62px;top:958px;width:509px">
  <h2>Clinical Label Stock</h2>
  <div class="service abs" style="left:1px;top:40px;width:508px">
    <div class="photo" style="background:linear-gradient(135deg,#f0f0f0,#c8d8cc,#fafafa)" role="img" aria-label="Stethoscope and pen on a medical form"></div>
    <div style="width:340px">
      <h3 style="margin-top:-2px">VeriStock™</h3>
      <p>VeriStock™ is a premium line of label products that we supply to the pharmaceutical industry. These label stocks are specifically designed...</p>
      <p class="more" style="margin-top:16px">Read More ››</p>
    </div>
  </div>
</section>

<div class="vrule abs"></div>

<section class="abs" style="left:608px;top:482px;width:342px">
  <h2>Our Services</h2>
  <div class="service abs" style="left:1px;top:35px;width:341px">
    <div class="photo" style="background:linear-gradient(135deg,#1a2a40,#7890a8,#223448)" role="img" aria-label="Stethoscope on a computer keyboard"></div>
    <div><h3>VeriServ™</h3><p>VeriServ™ is a contract clinical label generation service that provides you with ready to apply clinical labels specifically designed and produced for your clinical...</p><p class="more" style="margin-top:1px">Read More ››</p></div>
  </div>
  <div class="rule abs" style="left:0;top:138px;width:342px"></div>
  <div class="service abs" style="left:1px;top:151px;width:341px">
    <div class="photo" style="background:linear-gradient(135deg,#e8e8e8,#b0b8c0,#f4f4f4)" role="img" aria-label="Doctor working on a laptop"></div>
    <div><h3>VeriBook™</h3><p>VeriBook™ labels are multi-page clinical labels used to address the needs of multi-language studies. This enables user to prepare and ship clinical materials to multiple...</p><p class="more" style="margin-top:1px">Read More ››</p></div>
  </div>
  <div class="rule abs" style="left:0;top:270px;width:342px"></div>
  <div class="service abs" style="left:1px;top:282px;width:341px">
    <div class="photo" style="background:linear-gradient(135deg,#2aa8a8,#7fd0cc,#1e8c90)" role="img" aria-label="Medical worker holding a glowing heartbeat screen"></div>
    <div><h3>Clinical Randomizations</h3><p>Our systems can create randomization data for all types of CTM requirements. Patient randomization, material randomization and random...</p><p class="more" style="margin-top:1px">Read More ››</p></div>
  </div>
</section>

<section class="support abs">
  <h2 style="margin-top:-2px">User Support</h2>
  <div class="field" style="left:18px;top:46px;width:150px;height:25px">Name</div>
  <div class="field" style="left:178px;top:46px;width:150px;height:25px">Email Address</div>
  <div class="field" style="left:18px;top:77px;width:150px;height:25px">Contact No.</div>
  <div class="field" style="left:178px;top:77px;width:150px;height:25px">Company</div>
  <div class="field" style="left:18px;top:109px;width:310px;height:50px">Comments.</div>
  <a class="btn abs" style="left:222px;top:167px;width:104px;text-align:center;padding:0">Submit Now ››</a>
</section>

<footer class="site-footer abs">
  <nav class="foot-nav abs"><span>Home</span><span>About Us</span><span>Products</span><span>Services</span><span>User Support</span><span>Contact Us</span></nav>
  <p class="copy abs">Copyright © 2014. Veridane Works, Inc. All Right Reserved</p>
  <div class="social abs" aria-label="Social links"><span style="background:#3b5a9a"></span><span style="background:#2aa6e0"></span><span style="background:#f07b1a"></span><span style="background:#e02a26"></span></div>
</footer>
</body>
</html>
```